Civil engineering company | Billboard

We need a billboard design for Velmora- civil engineering company. We want big logo in the center of billboard and web site (www.velmora.hr) below the logo. Also, we want an subtle abstract pattern in the background. Dimensions of the billboard are: width :10 m, height: 2m. Design must be celan and modern.
Industry/Entity Type
Civil engineering
Font styles to use
Sans Serif
Colors
F0912C
F2A743
F7CA91
FBE8D2
FDF5EE
Requirements
Must have
- Logo and new unique pattern design for Velmroa company
Should not have
- pictures of construction machinery and tools

```html
<!DOCTYPE html>
<html lang="en">
<head>
<meta charset="utf-8">
<title>Velmora Billboard – 10 m × 2 m</title>
<link href="https://fonts.googleapis.com/css2?family=Cabin:wght@400;500;600&family=Open+Sans:wght@400&display=swap" rel="stylesheet">
<style>
  :root {
    --orange: #e39238;
    --orange-deep: #e8953a;
    --cream: #fffaf4;
    --black: #000000;
    --white: #ffffff;
    --grey: #666666;
    --grey-text: #555555;
    --measure: #e53935;
    --tick: #333333;
  }
  * { margin: 0; padding: 0; box-sizing: border-box; }
  html, body { width: 1200px; height: 1200px; overflow: hidden; background: var(--white); }
  .sheet { position: relative; width: 1200px; height: 1200px; }

  .billboard {
    position: absolute;
    left: 120px;
    width: 966px;
    height: 193px;
  }
  .billboard--dark { top: 268px; }
  .billboard--light { top: 680px; }

  .billboard__pattern { position: absolute; inset: 0; }
  .billboard--dark .billboard__pattern {
    background: linear-gradient(90deg, var(--black) 0%, #5a4a3a 14%, #b08858 30%, var(--orange) 40%, var(--orange) 62%, #b08858 74%, #5a4a3a 86%, var(--black) 100%);
  }
  .billboard--light .billboard__pattern {
    background: linear-gradient(90deg, var(--orange-deep) 0%, #f3c596 22%, #fbe8d2 34%, var(--cream) 46%, var(--cream) 56%, #fbe8d2 66%, #f3c596 80%, var(--orange-deep) 100%);
  }

  .brand {
    position: absolute;
    inset: 0;
    display: flex;
    flex-direction: column;
    align-items: center;
  }
  .brand__square {
    margin-top: 25px;
    width: 83px;
    height: 83px;
    border: 2px solid var(--white);
  }
  .brand__name {
    margin-top: 8px;
    font-family: "Cabin", sans-serif;
    font-weight: 500;
    font-size: 33px;
    letter-spacing: 4px;
    line-height: 1;
    text-transform: uppercase;
  }
  .brand__url {
    margin-top: 11px;
    font-family: "Cabin", sans-serif;
    font-weight: 500;
    font-size: 13.5px;
    letter-spacing: 0.3px;
  }
  .billboard--dark .brand__name { color: var(--black); }
  .billboard--dark .brand__url { color: var(--white); }
  .billboard--light .brand__square { border-color: var(--grey); }
  .billboard--light .brand__name { color: var(--orange); }
  .billboard--light .brand__url { color: var(--grey-text); }

  .dimension-label {
    position: absolute;
    font-family: "Open Sans", sans-serif;
    font-size: 21px;
    color: var(--measure);
    line-height: 1;
  }
  .dimension-lines { position: absolute; left: 0; top: 0; }
</style>
</head>
<body>
<div class="sheet">

  <svg class="dimension-lines" width="1200" height="1200" aria-hidden="true">
    <g fill="none" stroke-width="1">
      <line x1="97" y1="268" x2="97" y2="461" stroke="var(--measure)"/>
      <line x1="97" y1="268" x2="120" y2="268" stroke="var(--tick)" stroke-dasharray="2 2"/>
      <line x1="97" y1="461" x2="120" y2="461" stroke="var(--tick)" stroke-dasharray="2 2"/>
      <line x1="120" y1="482" x2="1086" y2="482" stroke="var(--measure)"/>
      <line x1="120" y1="461" x2="120" y2="482" stroke="var(--tick)" stroke-dasharray="2 2"/>
      <line x1="1086" y1="461" x2="1086" y2="482" stroke="var(--tick)" stroke-dasharray="2 2"/>

      <line x1="97" y1="680" x2="97" y2="873" stroke="var(--measure)"/>
      <line x1="97" y1="680" x2="120" y2="680" stroke="var(--tick)" stroke-dasharray="2 2"/>
      <line x1="97" y1="873" x2="120" y2="873" stroke="var(--tick)" stroke-dasharray="2 2"/>
      <line x1="120" y1="895" x2="1086" y2="895" stroke="var(--measure)"/>
      <line x1="120" y1="873" x2="120" y2="895" stroke="var(--tick)" stroke-dasharray="2 2"/>
      <line x1="1086" y1="873" x2="1086" y2="895" stroke="var(--tick)" stroke-dasharray="2 2"/>
    </g>
  </svg>

  <span class="dimension-label" style="left:48px; top:355px;">2M</span>
  <span class="dimension-label" style="left:581px; top:506px;">10M</span>
  <span class="dimension-label" style="left:48px; top:767px;">2M</span>
  <span class="dimension-label" style="left:581px; top:918px;">10M</span>

  <section class="billboard billboard--dark">
    <div class="billboard__pattern" role="img" aria-label="Faint repeating pattern of construction line icons over a black to orange to black gradient"></div>
    <div class="brand">
      <div class="brand__square"></div>
      <div class="brand__name">Velmora</div>
      <div class="brand__url">www.velmora.hr</div>
    </div>
  </section>

  <section class="billboard billboard--light">
    <div class="billboard__pattern" role="img" aria-label="Faint repeating pattern of construction line icons over an orange to cream to orange gradient"></div>
    <div class="brand">
      <div class="brand__square"></div>
      <div class="brand__name">Velmora</div>
      <div class="brand__url">www.velmora.hr</div>
    </div>
  </section>

</div>
</body>
</html>
```